Package design for a high-visibility children's commuter safety kit

As per the attached files (2+3) the kit contains a high-visibility vest, reflective snap bands as well as a novelty sticker and key ring. We have a particular layout in mind and the packaging design needs to accommodate these layout requirements. The package is 43cm in height and 26cm in width with a gap of 4cm across the top between the plastic covering the products and edge of the cardboard end and 5cm between the plastic covering and the right hand side of the cardboard. These gaps are the work area for the proposed designs on a black cardboard backing. In the design area we require the attached Brimvale logo
(File 1) and the description of the product (i.e. 'Child Commuter Safety Kit'). We are also considering having the contents listed for each item (e.g. Reflective vest/3 x reflective snap bands/Smiley sticker/Key ring). The design must keep in mind that the kits will be for children aged 5-15 years of age and primarily marketed towards children as well as concerned adults.

Plastic

```html
<!DOCTYPE html>
<html lang="en">
<head>
<meta charset="utf-8">
<title>Brimvale Child Commuter Safety Kit – Package</title>
<link rel="stylesheet" href="https://fonts.googleapis.com/css2?family=Arimo:ital,wght@0,400;0,700;1,700&display=swap">
<style>
  :root {
    --page: #ffffff;
    --card: #000000;
    --lime: #cddc3a;
    --lime-light: #b9d845;
    --lime-text: #d4e441;
    --grey: #8c8c8c;
    --tray: #1e1e1e;
    --white: #ffffff;
    --ink: #111111;
    --sign-red: #e42a2a;
    --sign-amber: #f2a33a;
    --sign-blue: #3aa9dc;
  }
  * { margin: 0; padding: 0; box-sizing: border-box; }
  html, body { width: 899px; height: 1200px; overflow: hidden; background: var(--page); }
  body { position: relative; font-family: "Arimo", Arial, sans-serif; }

  .package { position: absolute; left: 147px; top: 62px; width: 634px; height: 1048px; background: var(--card); overflow: hidden; }
  .frame-top { position: absolute; left: 1px; top: 99px; width: 510px; height: 4px; background: var(--lime); }
  .frame-side { position: absolute; left: 508px; top: 99px; width: 4px; height: 852px; background: var(--lime); }
  .age-band { position: absolute; left: 0; bottom: 0; width: 100%; height: 98px; background: linear-gradient(90deg, var(--lime-light), var(--lime)); }
  .age { position: absolute; right: 15px; top: 38px; font-weight: 700; font-size: 17px; color: var(--ink); }

  .brand { position: absolute; left: 36px; top: 22px; display: flex; align-items: center; gap: 10px; }
  .brand-mark { width: 26px; height: 26px; background: var(--lime); }
  .brand-name { font-size: 48px; color: var(--grey); letter-spacing: -1px; line-height: 1; }
  .product-title { position: absolute; left: 306px; top: 34px; color: var(--white); font-weight: 700; font-size: 16px; line-height: 18px; }

  .snap-band { position: absolute; left: 52px; top: 150px; width: 98px; height: 660px; background: linear-gradient(90deg, var(--lime-light), var(--lime)); }
  .snap-band-strip { position: absolute; left: 40px; top: 0; width: 15px; height: 100%; background: linear-gradient(180deg, #6e6e6e 0%, #444 45%, #151515 60%, #222 100%); }

  .sticker-tray { position: absolute; left: 242px; top: 147px; width: 136px; height: 135px; background: var(--tray); }
  .sticker { position: absolute; left: 8px; top: 8px; width: 120px; height: 120px; border-radius: 50%; background: var(--lime-text); }

  .keyring-tray { position: absolute; left: 256px; top: 288px; width: 109px; height: 135px; background: var(--tray); }
  .keyring { position: absolute; left: 12px; top: 7px; width: 83px; height: 119px; background: linear-gradient(90deg, var(--lime-light), var(--lime)); }
  .keyring-bar { position: absolute; left: 0; width: 100%; height: 11px; background: linear-gradient(180deg, #e6e6e6, #8a8a8a); }

  .vest { position: absolute; left: 177px; top: 443px; width: 274px; height: 363px; background: linear-gradient(90deg, var(--lime-light), var(--lime)); }
  .vest-strip { position: absolute; top: 4px; width: 73px; height: 359px; }
  .vest-strip.left { left: 13px; background: linear-gradient(180deg, #6a6a6a 0%, #5a5a5a 35%, #1c1c1c 55%, #222 100%); }
  .vest-strip.right { left: 181px; background: linear-gradient(180deg, #7c7c7c 0%, #6a6a6a 35%, #3a3a3a 55%, #4a4a4a 100%); }

  .contents { position: absolute; left: 510px; top: 248px; width: 124px; list-style: none; }
  .contents li { position: absolute; left: 0; width: 124px; background: var(--lime); color: var(--ink); font-style: italic; font-weight: 700; font-size: 13px; text-align: center; line-height: 15px; padding: 2px 0; transform: rotate(-6deg); transform-origin: left center; }

  .sign { position: absolute; left: 533px; }
  .decor { position: absolute; }
</style>
</head>
<body>
<main class="package">
  <div class="decor" role="img" aria-label="Scattered light bubble circles" style="left:440px;top:0;width:194px;height:240px;background:radial-gradient(circle at 70% 50%, rgba(220,230,190,0.12), transparent 70%);"></div>
  <div class="decor" role="img" aria-label="Scattered light bubble circles" style="left:10px;top:840px;width:350px;height:110px;background:radial-gradient(circle at 40% 50%, rgba(220,220,220,0.08), transparent 70%);"></div>

  <div class="brand">
    <span class="brand-mark"></span>
    <span class="brand-name">Brimvale</span>
  </div>
  <h1 class="product-title">Child Commuter<br>Safety Kit</h1>

  <div class="frame-top"></div>
  <div class="frame-side"></div>

  <div class="snap-band"><div class="snap-band-strip"></div></div>

  <div class="sticker-tray"><div class="sticker" role="img" aria-label="Round smiley sticker"></div></div>

  <div class="keyring-tray">
    <div class="keyring">
      <div class="keyring-bar" style="top:78px"></div>
      <div class="keyring-bar" style="top:98px"></div>
    </div>
  </div>

  <div class="vest">
    <div class="vest-strip left"></div>
    <div class="vest-strip right"></div>
  </div>

  <ul class="contents">
    <li style="top:10px">Reflective vest</li>
    <li style="top:40px">Reflective<br>Snap Bands</li>
    <li style="top:88px">Smiley sticker</li>
    <li style="top:128px">Key ring</li>
  </ul>

  <svg class="sign" style="top:516px" width="80" height="68" viewBox="0 0 80 68" aria-label="Warning sign">
    <polygon points="40,4 76,64 4,64" fill="var(--white)" stroke="var(--sign-red)" stroke-width="7" stroke-linejoin="round"/>
    <rect x="36.5" y="24" width="7" height="24" rx="2" fill="var(--ink)"/>
    <circle cx="40" cy="55" r="4" fill="var(--ink)"/>
  </svg>
  <div class="sign" role="img" aria-label="Children crossing warning sign" style="top:608px;width:76px;height:70px;background:var(--sign-amber);clip-path:polygon(50% 0,100% 100%,0 100%);"></div>
  <div class="sign" role="img" aria-label="Pedestrian crossing road sign" style="top:708px;width:76px;height:76px;border:3px solid var(--white);border-radius:6px;background:var(--sign-blue);"></div>
  <div class="sign" role="img" aria-label="Child cyclist road sign" style="top:818px;width:76px;height:72px;border:3px solid var(--white);border-radius:6px;background:var(--sign-blue);"></div>

  <div class="age-band"><p class="age">5-15 years</p></div>
</main>
</body>
</html>
```